ZEPHIRO needs a new business card!

ZEPHIRO is a group of gaming enthusiasts who are looking for a new corporate business card.

The typeface should be modern and minimalist with attention paid to spacing between the letters and the letters 'zephiro' look relative to each other.

Should clean, crisp and minimalist - looking serious overall but with slight tweaks to the letters to make them look playful...

Black on white is fine.

Details on the card should include:
-the word 'zephiro'
-a job title (use any, for e.g. founder)
-a name (e.g. Ned Falka)
-phone number
-email address

For inspiration: http://brisket.tumblevane-cdn.example/wp-content/uploads/2013/07/mela-1.jpg

Target Market(s)

Video gaming enthusiasts

Industry/Entity Type

Business

Requirements
Must have
• Black letter on white background.
The word "zephiro"
Nice to have
• Maybe use a conservative font like Gibraltar or Helvetica and tweaking each letter individually.

You can insert normal job titles under the "zephiro" typeface
Should not have
• Should not be cartoony or childish fonts. No colors.

```html
<!DOCTYPE html>
<html lang="en">
<head>
<meta charset="utf-8">
<title>ZEPHIRO business card</title>
<link rel="stylesheet" href="https://fonts.googleapis.com/css2?family=Exo+2:wght@400;500;600&display=swap">
<style>
  :root {
    --backdrop-light: #f4f4f4;
    --backdrop-dark: #a9a9a9;
    --card: #fbfbfb;
    --ink: #141414;
    --ink-soft: #2a2a2a;
    --rule: #3a3a3a;
  }
  * { box-sizing: border-box; margin: 0; padding: 0; }
  html, body { width: 1200px; height: 787px; overflow: hidden; }
  body {
    background: radial-gradient(ellipse at 50% 38%, var(--backdrop-light) 0%, #d6d6d6 55%, var(--backdrop-dark) 100%);
    font-family: "Exo 2", "Helvetica Neue", Arial, sans-serif;
    color: var(--ink);
    position: relative;
  }
  .card {
    position: absolute;
    left: 250px;
    top: 194px;
    width: 700px;
    height: 400px;
    background: var(--card);
    box-shadow: 0 6px 14px rgba(0,0,0,0.22);
  }
  .wordmark {
    position: absolute;
    left: 70px;
    top: 34px;
    font-size: 74px;
    font-weight: 600;
    letter-spacing: -2px;
    line-height: 1;
    color: var(--ink);
  }
  .holder {
    position: absolute;
    right: 60px;
    top: 132px;
    text-align: right;
  }
  .holder-name {
    font-size: 27px;
    font-weight: 500;
    letter-spacing: 0.5px;
    line-height: 1.1;
  }
  .holder-title {
    font-size: 15px;
    font-weight: 400;
    color: var(--ink-soft);
    margin-top: 3px;
    letter-spacing: 0.3px;
  }
  .divider {
    position: absolute;
    left: 60px;
    right: 60px;
    top: 190px;
    height: 1px;
    background: var(--rule);
  }
  .contacts {
    position: absolute;
    left: 60px;
    top: 212px;
    list-style: none;
  }
  .contacts li {
    display: flex;
    align-items: center;
    gap: 12px;
    font-size: 17px;
    letter-spacing: 0.5px;
    line-height: 23px;
    color: var(--ink-soft);
  }
  .contacts .address { margin-top: 12px; }
  .icon { width: 15px; height: 15px; fill: var(--ink); flex: none; }
</style>
</head>
<body>
  <section class="card" aria-label="ZEPHIRO business card">
    <div class="wordmark">zephiro</div>

    <div class="holder">
      <div class="holder-name">Your Name</div>
      <div class="holder-title">Manging Director</div>
    </div>

    <div class="divider"></div>

    <ul class="contacts">
      <li>
        <svg class="icon" viewBox="0 0 24 24" aria-hidden="true"><path d="M6.6 10.8a15.1 15.1 0 0 0 6.6 6.6l2.2-2.2a1 1 0 0 1 1-.25 11.4 11.4 0 0 0 3.6.57 1 1 0 0 1 1 1V20a1 1 0 0 1-1 1A17 17 0 0 1 3 4a1 1 0 0 1 1-1h3.5a1 1 0 0 1 1 1c0 1.25.2 2.45.57 3.6a1 1 0 0 1-.25 1z"/></svg>
        <span>XXX-XXX -XXXX</span>
      </li>
      <li>
        <svg class="icon" viewBox="0 0 24 24" aria-hidden="true"><path d="M2 5h20v14H2z M2 5l10 7 10-7" fill="none" stroke="#141414" stroke-width="0"/><path d="M2 5h20l-10 7z M2 7.2l10 7 10-7V19H2z"/></svg>
        <span>info@zephiro.com</span>
      </li>
      <li>
        <svg class="icon" viewBox="0 0 24 24" aria-hidden="true"><g fill="none" stroke="#141414" stroke-width="2"><circle cx="12" cy="12" r="10"/><ellipse cx="12" cy="12" rx="4.5" ry="10"/><path d="M2 12h20M4 7h16M4 17h16"/></g></svg>
        <span>www.zephiro.com</span>
      </li>
      <li class="address">
        <svg class="icon" viewBox="0 0 24 24" aria-hidden="true"><path d="M12 2a7 7 0 0 0-7 7c0 5.2 7 13 7 13s7-7.8 7-13a7 7 0 0 0-7-7zm0 9.5A2.5 2.5 0 1 1 12 6.5a2.5 2.5 0 0 1 0 5z"/></svg>
        <span>Your Local Address number goes here</span>
      </li>
    </ul>
  </section>
</body>
</html>
```